Welcome Package Cover

We want to design a new cover for our welcome package. The dimensions are 4 1/4" x 9". We are a church in London Ontario called HARBOR Church. Our website is www.harborvellmont.ca
We don't want it to be churchy or religious looking. We want it to be fresh and youthful.
Can use backgrounds unique to London Ontario Canada
I will attach our logo designs.
Religious

```html
<!DOCTYPE html>
<html lang="en">
<head>
<meta charset="utf-8">
<title>HARBOR Church — Welcome Package Cover</title>
<link rel="stylesheet" href="https://fonts.googleapis.com/css2?family=Bebas+Neue&display=swap">
<style>
  :root {
    --frame: #e4e4e2;
    --sky-top: #d6d6d4;
    --sky-bottom: #9a9a98;
    --grass: #3c3c3a;
    --olive: #b5b21e;
    --navy: #141466;
    --crimson: #e3145c;
    --shade: #1c1418;
    --green: #1f8a2c;
    --magenta: #c21cb2;
    --rust: #d23a12;
    --cyan: #1c90d2;
    --lavender: #cfcde6;
    --blush: #f0c8e0;
    --ink: #f4f2ee;
    --title-shadow: rgba(90, 60, 70, 0.45);
  }
  * { margin: 0; padding: 0; box-sizing: border-box; }
  html, body {
    width: 1200px;
    height: 2540px;
    overflow: hidden;
    background: var(--frame);
  }
  .cover {
    position: relative;
    width: 1200px;
    height: 2540px;
    background: var(--frame);
    overflow: hidden;
  }
  .photo {
    position: absolute;
    left: 47px; top: 47px;
    width: 1106px; height: 2446px;
    background: linear-gradient(180deg,
      var(--sky-top) 0%,
      #b8b8b6 35%,
      var(--sky-bottom) 85%,
      #6a6a68 86.5%,
      var(--grass) 90%,
      #2e2e2c 100%);
  }
  .block { position: absolute; mix-blend-mode: multiply; }
  .block--olive    { left: 47px;  top: 47px;   width: 270px; height: 556px; background: var(--olive); opacity: .9; }
  .block--lavender { left: 0;     top: 540px;  width: 47px;  height: 1700px; background: var(--lavender); opacity: .8; }
  .block--navy     { left: 0;     top: 540px;  width: 138px; height: 380px; background: var(--navy); opacity: .95; }
  .block--crimson  { left: 85px;  top: 836px;  width: 709px; height: 518px; background: var(--crimson); opacity: .9; }
  .block--green    { left: 720px; top: 736px;  width: 433px; height: 470px; background: var(--green); opacity: .9; }
  .block--shade    { left: 720px; top: 836px;  width: 74px;  height: 370px; background: var(--shade); opacity: .85; }
  .block--magenta  { left: 1026px; top: 1206px; width: 127px; height: 931px; background: var(--magenta); opacity: .9; }
  .block--rust     { left: 47px;  top: 1206px; width: 196px; height: 455px; background: var(--rust); opacity: .9; }
  .block--dark     { left: 47px;  top: 1661px; width: 196px; height: 127px; background: var(--shade); opacity: .8; }
  .block--cyan     { left: 47px;  top: 1661px; width: 499px; height: 519px; background: var(--cyan); opacity: .85; }
  .block--blush    { left: 0;     top: 2180px; width: 47px;  height: 313px; background: var(--blush); opacity: .9; }

  .title {
    position: absolute;
    left: 0; top: 880px;
    width: 1200px;
    text-align: center;
    font-family: "Bebas Neue", "Oswald", sans-serif;
    font-size: 330px;
    line-height: 1;
    letter-spacing: 6px;
    color: var(--ink);
    text-shadow: 22px 18px 0 var(--title-shadow);
  }
  .brand {
    position: absolute;
    left: 265px; top: 2200px;
    display: flex;
    align-items: center;
    gap: 40px;
  }
  .brand__name {
    font-family: "Bebas Neue", "Oswald", sans-serif;
    font-size: 92px;
    line-height: 1;
    letter-spacing: 1px;
    color: var(--ink);
  }
  .brand__mark {
    width: 170px; height: 170px;
    border-radius: 50%;
    background: var(--ink);
  }
</style>
</head>
<body>
  <main class="cover">
    <div class="photo" role="img" aria-label="Black and white photo of a young woman jumping joyfully with arms raised against a cloudy sky above a grassy field"></div>

    <div class="block block--lavender"></div>
    <div class="block block--olive"></div>
    <div class="block block--navy"></div>
    <div class="block block--crimson"></div>
    <div class="block block--green"></div>
    <div class="block block--shade"></div>
    <div class="block block--magenta"></div>
    <div class="block block--rust"></div>
    <div class="block block--cyan"></div>
    <div class="block block--dark"></div>
    <div class="block block--blush"></div>

    <h1 class="title">WELCOME</h1>

    <div class="brand">
      <span class="brand__name">HARBOR CHURCH</span>
      <span class="brand__mark" aria-hidden="true"></span>
    </div>
  </main>
</body>
</html>
```